Business Card and Stationary
BrookLamp Consutling
Professional
Peter Varsiklo
8276 Wimbrell Lane
Corvale, IN 43092
pvarsiklo@brooklampconsulting.com
brooklampconsulting.com

```html
<!DOCTYPE html>
<html lang="en">
<head>
<meta charset="utf-8">
<title>BrookLamp Consulting – Business Cards</title>
<link rel="stylesheet" href="https://fonts.googleapis.com/css2?family=Open+Sans:wght@400;700&display=swap">
<style>
  :root {
    --bg: #ececec;
    --green: #8cc63f;
    --green-light: #a6d664;
    --ink: #3a3a3a;
    --ink-soft: #5f5f5f;
    --dark-band: #3d3d3d;
    --white: #ffffff;
    --paper-grey: #e2e2e2;
  }
  html, body {
    margin: 0;
    padding: 0;
    width: 1200px;
    height: 763px;
    overflow: hidden;
    background: var(--bg);
    font-family: "Open Sans", Arial, sans-serif;
  }
  .canvas { position: relative; width: 1200px; height: 763px; }
  .card {
    position: absolute;
    border-radius: 12px;
    overflow: hidden;
    box-shadow: 0 3px 10px rgba(0,0,0,0.18);
  }
  .wordmark { position: absolute; font-weight: 700; line-height: 1; text-align: center; white-space: nowrap; }
  .wordmark .name { display: block; }
  .wordmark .sub { display: block; }

  /* Front card */
  .card-front {
    left: 89px; top: 139px; width: 494px; height: 283px;
    background: var(--white);
    z-index: 2;
  }
  .front-texture {
    position: absolute; left: 40px; top: 26px; width: 150px; height: 110px;
    background: radial-gradient(ellipse at center, #e6e6e6, rgba(255,255,255,0) 70%);
  }
  .card-front .wordmark { left: 19px; top: 174px; color: var(--ink); }
  .card-front .wordmark .name { font-size: 30px; }
  .card-front .wordmark .sub { font-size: 12px; letter-spacing: 5.5px; margin-top: 4px; }
  .divider {
    position: absolute; left: 230px; top: 65px; width: 1px; height: 96px;
    background: #bdbdbd;
  }
  .contact { position: absolute; left: 254px; top: 80px; color: var(--ink-soft); font-size: 11px; line-height: 1.45; }
  .contact .person { color: var(--green); font-size: 18px; font-weight: 700; line-height: 1.2; margin-bottom: 11px; }
  .contact .gap { height: 12px; }
  .band { position: absolute; top: 245px; height: 24px; }
  .band-green { left: 0; width: 283px; background: var(--green); }
  .band-dark { left: 283px; width: 211px; background: var(--dark-band); color: var(--white);
    font-size: 10px; line-height: 24px; padding-left: 12px; box-sizing: border-box; }

  /* Green back */
  .card-green {
    left: 631px; top: 84px; width: 502px; height: 276px;
    background: var(--green);
    z-index: 1;
  }
  .card-green .texture {
    position: absolute; left: 40px; top: 0; width: 300px; height: 230px;
    background: radial-gradient(ellipse at center, var(--green-light), rgba(140,198,63,0) 70%);
  }
  .card-green .wordmark { right: 14px; bottom: 22px; color: var(--white); }

  /* White back */
  .card-white {
    left: 372px; top: 403px; width: 499px; height: 286px;
    background: linear-gradient(135deg, var(--white) 45%, var(--paper-grey));
    z-index: 1;
  }
  .card-white .texture {
    position: absolute; left: 40px; top: 17px; width: 310px; height: 252px;
    background: radial-gradient(ellipse at center, #e4e4e4, rgba(255,255,255,0) 70%);
  }
  .card-white .wordmark { right: 14px; bottom: 28px; color: var(--ink); }

  .back .wordmark .name { font-size: 32px; }
  .back .wordmark .sub { font-size: 13px; letter-spacing: 6px; margin-top: 4px; }
</style>
</head>
<body>
<main class="canvas">

  <section class="card card-green back" aria-label="Card back, green">
    <div class="texture" role="img" aria-label="Woven tonal pattern area"></div>
    <div class="wordmark"><span class="name">BrookLamp</span><span class="sub">Consulting</span></div>
  </section>

  <section class="card card-white back" aria-label="Card back, white">
    <div class="texture" role="img" aria-label="Woven tonal pattern area"></div>
    <div class="wordmark"><span class="name">BrookLamp</span><span class="sub">Consulting</span></div>
  </section>

  <section class="card card-front" aria-label="Card front">
    <div class="front-texture" role="img" aria-label="Woven tonal pattern area"></div>
    <div class="wordmark"><span class="name">BrookLamp</span><span class="sub">Consulting</span></div>
    <div class="divider"></div>
    <div class="contact">
      <div class="person">Peter Varsiklo</div>
      <div>8276 Wimbrell Lane</div>
      <div>Corvale, IN 43092</div>
      <div class="gap"></div>
      <div>Phone: 812-555-0182</div>
      <div>pvarsiklo@brooklampconsulting.com</div>
    </div>
    <div class="band band-green"></div>
    <div class="band band-dark">www.brooklampconsulting.com</div>
  </section>

</main>
</body>
</html>
```